Heater product information sheets

I need the two product information sheets organized and laid out in a clean, easy to read attractive manner. These sheets are to advertise propane heaters for outdoor use and for wholesale to propane distributors, restaurants and homeowners that need to have propane heat as the winter ends and spring begins. They will be used for chilly evenings when people want to be outside eating, drinking and being social.
Updates

Low design quality

Target Market(s)

Restaurants, hospitality industry, special events, party rental companies, home owners with backyards

Font styles to use
Sans Serif

Requirements
Must have
• My logo in the document instead of k. Dahlby and company
Nice to have
• I would like to see Fire illustrated coming up the heaters and on the round glass, show it up the middle of the glass tube propane heater.

```html
<!DOCTYPE html>
<html lang="en">
<head>
<meta charset="utf-8">
<title>Propane Heater Product Sheets</title>
<link rel="stylesheet" href="https://fonts.googleapis.com/css2?family=Roboto:wght@900&family=Arimo:wght@400;700&display=swap">
<style>
  :root {
    --orange: #f07c2a;
    --orange-soft: #f38d4e;
    --ink: #1b1b1b;
    --black: #0e0e0e;
    --white: #ffffff;
    --paper: #fbfbfb;
    --backdrop: #e6e6e4;
  }
  * { box-sizing: border-box; margin: 0; padding: 0; }
  html, body { width: 1200px; height: 796px; overflow: hidden; background: var(--backdrop); }
  .canvas { position: relative; width: 1200px; height: 796px; }

  .sheet-frame { position: absolute; top: 62px; width: 506px; height: 658px; box-shadow: 0 4px 14px rgba(0,0,0,.25); overflow: hidden; }
  .sheet-frame--left { left: 75px; }
  .sheet-frame--right { left: 623px; }
  .sheet { position: absolute; top: 0; left: 0; width: 610px; height: 793px; transform: scale(0.8295); transform-origin: 0 0; background: var(--paper); font-family: "Arimo", sans-serif; color: var(--ink); overflow: hidden; }
  .sheet__art { position: absolute; inset: 0; width: 610px; height: 793px; }

  .title { position: absolute; left: 32px; top: 38px; font-family: "Roboto", sans-serif; font-weight: 900; font-size: 45px; line-height: 57px; letter-spacing: 1.5px; color: var(--white); text-transform: uppercase; white-space: nowrap; }
  .title__accent { color: var(--orange); }
  .title-rule { position: absolute; left: 318px; top: 42px; width: 1px; height: 155px; background: rgba(255,255,255,.55); }

  .uses { position: absolute; left: 337px; top: 57px; list-style: none; }
  .uses li { position: relative; padding-left: 20px; margin-bottom: 12px; font-weight: 700; font-size: 12.5px; line-height: 15px; color: var(--white); text-transform: uppercase; }
  .uses svg { position: absolute; left: 0; top: 1px; width: 13px; height: 13px; }

  .heading { position: absolute; font-family: "Arimo", sans-serif; font-weight: 700; font-size: 23px; letter-spacing: 2px; color: var(--ink); text-transform: uppercase; }
  .heading--specs { left: 33px; top: 270px; }
  .heading--details { left: 36px; top: 426px; }

  .specs { position: absolute; left: 35px; top: 304px; list-style: none; }
  .specs li { font-size: 12px; line-height: 18.7px; color: var(--white); letter-spacing: .5px; text-transform: uppercase; padding-left: 11px; position: relative; }
  .specs li::before { content: ""; position: absolute; left: 0; top: 8px; width: 4px; height: 4px; border-radius: 50%; background: var(--white); }

  .details { position: absolute; left: 34px; top: 459px; list-style: none; }
  .details li { font-size: 12px; line-height: 20px; color: var(--ink); padding-left: 10px; position: relative; }
  .details li::before { content: ""; position: absolute; left: 0; top: 9px; width: 4px; height: 4px; border-radius: 50%; background: var(--orange); }

  .note { position: absolute; top: 515px; width: 112px; text-align: center; color: var(--white); }
  .note--left { left: 469px; }
  .note--right { left: 476px; }
  .note__title { font-weight: 700; font-size: 24px; letter-spacing: 1.5px; line-height: 26px; }
  .note__price { font-size: 10.5px; line-height: 13px; margin-top: 2px; }
  .note__fine { font-size: 8px; line-height: 11px; }

  .contact { position: absolute; right: 15px; top: 690px; text-align: right; color: var(--white); }
  .contact__lead { font-weight: 700; font-size: 14px; letter-spacing: .6px; color: var(--orange); line-height: 18px; }
  .contact__company { font-weight: 700; font-size: 14px; letter-spacing: .6px; line-height: 18px; margin-bottom: 4px; text-transform: uppercase; }
  .contact__line { font-size: 12.5px; line-height: 18px; padding-right: 22px; position: relative; }
  .contact__line svg { position: absolute; right: 0; top: 3px; width: 12px; height: 12px; }

  .brand { position: absolute; left: 35px; top: 722px; display: flex; align-items: center; gap: 8px; }
  .brand__dot { width: 18px; height: 18px; border-radius: 50%; background: var(--orange); }
  .brand__name { font-family: "Arimo", sans-serif; font-weight: 700; font-size: 17px; line-height: 20px; color: var(--ink); width: 130px; }
</style>
</head>
<body>
<main class="canvas">

  <div class="sheet-frame sheet-frame--left">
    <article class="sheet">
      <svg class="sheet__art" viewBox="0 0 610 793">
        <defs>
          <linearGradient id="patioA" x1="0" y1="0" x2="1" y2="1">
            <stop offset="0" stop-color="#1d231b"/><stop offset=".5" stop-color="#4a5343"/><stop offset="1" stop-color="#2b3127"/>
          </linearGradient>
          <linearGradient id="heaterA" x1="0" y1="0" x2="0" y2="1">
            <stop offset="0" stop-color="#d9d9d9"/><stop offset=".35" stop-color="#6b6b6b"/><stop offset="1" stop-color="#121212"/>
          </linearGradient>
          <linearGradient id="paperA" x1="0" y1="0" x2="1" y2="1">
            <stop offset="0" stop-color="#ffffff"/><stop offset=".6" stop-color="#f2f2f2"/><stop offset="1" stop-color="#ffffff"/>
          </linearGradient>
        </defs>
        <rect x="0" y="0" width="610" height="430" fill="url(#patioA)" role="img" aria-label="Photo of an evening garden patio with outdoor seating"/>
        <path d="M0 415 C250 410 480 330 610 230 L610 793 L0 793 Z" fill="url(#paperA)"/>
        <path d="M0 250 C200 258 450 230 610 115 L610 230 C480 330 250 410 0 415 Z" fill="var(--orange)" opacity=".93"/>
        <rect x="425" y="228" width="115" height="426" rx="30" fill="url(#heaterA)" role="img" aria-label="Product photo of a black outdoor mushroom-top propane patio heater"/>
        <circle cx="525" cy="568" r="57" fill="var(--orange-soft)"/>
        <path d="M190 793 C270 690 420 655 610 645 L610 658 C430 666 290 700 218 793 Z" fill="var(--orange)"/>
        <path d="M218 793 C290 700 430 666 610 658 L610 793 Z" fill="var(--black)"/>
      </svg>

      <h1 class="title">Outdoor<br>Propane<br><span class="title__accent">Heater</span></h1>
      <div class="title-rule"></div>
      <ul class="uses">
        <li><svg viewBox="0 0 13 13"><circle cx="6.5" cy="6.5" r="6.5" fill="#f07c2a"/><path d="M3.5 6.7 5.6 8.7 9.5 4.5" stroke="#fff" stroke-width="1.8" fill="none"/></svg>Rentals for live events</li>
        <li><svg viewBox="0 0 13 13"><circle cx="6.5" cy="6.5" r="6.5" fill="#f07c2a"/><path d="M3.5 6.7 5.6 8.7 9.5 4.5" stroke="#fff" stroke-width="1.8" fill="none"/></svg>Rentals for restaurants<br>&amp; catering halls</li>
        <li><svg viewBox="0 0 13 13"><circle cx="6.5" cy="6.5" r="6.5" fill="#f07c2a"/><path d="M3.5 6.7 5.6 8.7 9.5 4.5" stroke="#fff" stroke-width="1.8" fill="none"/></svg>Purchase for your home<br>or business</li>
      </ul>

      <h2 class="heading heading--specs">Specifications</h2>
      <ul class="specs">
        <li>Powerful 48,000 BTU</li>
        <li>Black powder coated finish</li>
        <li>Uses 20 lbs. propane tank</li>
        <li>CE, GS, AGA, CSA, with ETL certificate<br>and RoHS approved</li>
      </ul>

      <h2 class="heading heading--details">Additional Details</h2>
      <ul class="details">
        <li>Commercial Quality</li>
        <li>For Outdoor Use Only</li>
        <li>Conforms to ANSI STD Z83.26-2014 Certified<br>to CSA STD 2.37-2014 Gas- fired outdoor infrared patio heaters</li>
        <li>Safety Auto Shut Off Switch</li>
        <li>Thermostatic Control</li>
        <li>Base Diameter 17” - Anti-Tip Design</li>
        <li>Standard Wheels - Tilt &amp; Move</li>
        <li>Run time: 8-10 hours with standard 20 lbs. Propane tank</li>
        <li>88” Tall</li>
        <li>Heating Area: 200 sq. ft</li>
      </ul>

      <div class="note note--left">
        <div class="note__title">NOTE</div>
        <div class="note__price">Price: Starting at<br>$250 each</div>
        <div class="note__fine">Assembly &amp; Delivery available<br>upon request. Discounts<br>for large quantity orders</div>
      </div>

      <div class="brand"><span class="brand__dot"></span><span class="brand__name">Brightfield Party Rental</span></div>

      <div class="contact">
        <div class="contact__lead">TO RENT OR PURCHASE:</div>
        <div class="contact__company">K. Dahlby &amp; Company</div>
        <div class="contact__line">555-014-2290<svg viewBox="0 0 12 12"><circle cx="6" cy="6" r="6" fill="#f07c2a"/><path d="M4 3.2 5.2 4.6 4.6 5.4C5 6.3 5.7 7 6.6 7.4L7.4 6.8 8.8 8 8.2 9C6 8.8 3.2 6 3 3.8Z" fill="#fff"/></svg></div>
        <div class="contact__line">Nora@brightfieldrental.com<svg viewBox="0 0 12 12"><circle cx="6" cy="6" r="6" fill="#f07c2a"/><rect x="3" y="4" width="6" height="4.2" fill="none" stroke="#fff" stroke-width="1"/><path d="M3 4 6 6.4 9 4" stroke="#fff" stroke-width="1" fill="none"/></svg></div>
        <div class="contact__line">42 Mill Street Hartwell, NJ 07099<svg viewBox="0 0 12 12"><circle cx="6" cy="6" r="6" fill="#f07c2a"/><path d="M6 9.5C4.4 7.6 3.8 6.5 3.8 5.2A2.2 2.2 0 0 1 8.2 5.2C8.2 6.5 7.6 7.6 6 9.5Z" fill="#fff"/></svg></div>
      </div>
    </article>
  </div>

  <div class="sheet-frame sheet-frame--right">
    <article class="sheet">
      <svg class="sheet__art" viewBox="0 0 610 793">
        <defs>
          <linearGradient id="patioB" x1="0" y1="0" x2="1" y2="1">
            <stop offset="0" stop-color="#1d231b"/><stop offset=".5" stop-color="#4a5343"/><stop offset="1" stop-color="#2b3127"/>
          </linearGradient>
          <linearGradient id="heaterB" x1="0" y1="0" x2="0" y2="1">
            <stop offset="0" stop-color="#d4d4d4"/><stop offset=".5" stop-color="#ececec"/><stop offset=".62" stop-color="#2a2a2a"/><stop offset="1" stop-color="#101010"/>
          </linearGradient>
          <linearGradient id="paperB" x1="0" y1="0" x2="1" y2="1">
            <stop offset="0" stop-color="#ffffff"/><stop offset=".6" stop-color="#f2f2f2"/><stop offset="1" stop-color="#ffffff"/>
          </linearGradient>
        </defs>
        <rect x="0" y="0" width="610" height="430" fill="url(#patioB)" role="img" aria-label="Photo of an evening garden patio with outdoor seating"/>
        <path d="M0 415 C250 410 480 330 610 230 L610 793 L0 793 Z" fill="url(#paperB)"/>
        <path d="M0 250 C200 258 450 230 610 115 L610 230 C480 330 250 410 0 415 Z" fill="var(--orange)" opacity=".93"/>
        <rect x="395" y="238" width="160" height="414" rx="30" fill="url(#heaterB)" role="img" aria-label="Product photo of a glass tube propane patio heater with black base"/>
        <circle cx="532" cy="568" r="57" fill="var(--orange-soft)"/>
        <path d="M190 793 C270 690 420 655 610 645 L610 658 C430 666 290 700 218 793 Z" fill="var(--orange)"/>
        <path d="M218 793 C290 700 430 666 610 658 L610 793 Z" fill="var(--black)"/>
      </svg>

      <h1 class="title">Glass Tube<br>Propane<br><span class="title__accent">Heaters</span></h1>
      <div class="title-rule"></div>
      <ul class="uses">
        <li><svg viewBox="0 0 13 13"><circle cx="6.5" cy="6.5" r="6.5" fill="#f07c2a"/><path d="M3.5 6.7 5.6 8.7 9.5 4.5" stroke="#fff" stroke-width="1.8" fill="none"/></svg>Rentals for live events</li>
        <li><svg viewBox="0 0 13 13"><circle cx="6.5" cy="6.5" r="6.5" fill="#f07c2a"/><path d="M3.5 6.7 5.6 8.7 9.5 4.5" stroke="#fff" stroke-width="1.8" fill="none"/></svg>Rentals for restaurants<br>&amp; catering halls</li>
        <li><svg viewBox="0 0 13 13"><circle cx="6.5" cy="6.5" r="6.5" fill="#f07c2a"/><path d="M3.5 6.7 5.6 8.7 9.5 4.5" stroke="#fff" stroke-width="1.8" fill="none"/></svg>Purchase for your home<br>or business</li>
      </ul>

      <h2 class="heading heading--specs">Specifications</h2>
      <ul class="specs">
        <li>Powerful 48,000 BTU</li>
        <li>Black powder coated finish</li>
        <li>Uses 20 lbs. propane tank</li>
        <li>CE, GS, AGA, CSA, with ETL certificate<br>and RoHS approved</li>
      </ul>

      <h2 class="heading heading--details">Additional Details</h2>
      <ul class="details">
        <li>Commercial Quality</li>
        <li>For Outdoor Use Only</li>
        <li>Conforms to ANSI STD Z83.26-2014 Certified to<br>CSA STD 2.37-2014 Gas- fired outdoor infrared patio heaters</li>
        <li>Safety Auto Shut Off Switch</li>
        <li>Thermostatic Control</li>
        <li>Base Diameter 17” - Anti-Tip Design</li>
        <li>Standard Wheels - Tilt &amp; Move</li>
        <li>Run time: 8-10 hours with standard 20 lbs. Propane tank</li>
        <li>96” Tall</li>
        <li>Heating Area: 200 sq. ft</li>
      </ul>

      <div class="note note--right">
        <div class="note__title">NOTE</div>
        <div class="note__price">Price: Starting at<br>$250 each</div>
        <div class="note__fine">Assembly &amp; Delivery available<br>upon request. Discounts<br>for large quantity orders</div>
      </div>

      <div class="brand"><span class="brand__dot"></span><span class="brand__name">Brightfield Party Rental</span></div>

      <div class="contact">
        <div class="contact__lead">TO RENT OR PURCHASE:</div>
        <div class="contact__company">K. Dahlby &amp; Company</div>
        <div class="contact__line">555-014-2290<svg viewBox="0 0 12 12"><circle cx="6" cy="6" r="6" fill="#f07c2a"/><path d="M4 3.2 5.2 4.6 4.6 5.4C5 6.3 5.7 7 6.6 7.4L7.4 6.8 8.8 8 8.2 9C6 8.8 3.2 6 3 3.8Z" fill="#fff"/></svg></div>
        <div class="contact__line">Nora@brightfieldrental.com<svg viewBox="0 0 12 12"><circle cx="6" cy="6" r="6" fill="#f07c2a"/><rect x="3" y="4" width="6" height="4.2" fill="none" stroke="#fff" stroke-width="1"/><path d="M3 4 6 6.4 9 4" stroke="#fff" stroke-width="1" fill="none"/></svg></div>
        <div class="contact__line">42 Mill Street Hartwell, NJ 07099<svg viewBox="0 0 12 12"><circle cx="6" cy="6" r="6" fill="#f07c2a"/><path d="M6 9.5C4.4 7.6 3.8 6.5 3.8 5.2A2.2 2.2 0 0 1 8.2 5.2C8.2 6.5 7.6 7.6 6 9.5Z" fill="#fff"/></svg></div>
      </div>
    </article>
  </div>

</main>
</body>
</html>
```